Design the product packaging for a video brochure

We are going to provide a video brochure to potential clients - the video brochure will be printed with our company and software information on it. We are looking for an eye catching design that follows our standards and color scheme that can be printed on the outside packaging of the video message being delivered in the video greeting card like package. We want the wording and styling to be timeless so we don't have to reprint/re-design this packaging as we upgrade our systems or message contained inside the video. The template provided is for a 7inch screen and shows how the template is wrapped around the screen to create the packaging. I have also provided an example of the product for your reference - you are designing the outside paper packaging of this card.

I just posted this today and it closed the same day - This is NOT what I wanted... I have extended the deadline.

• We want this to go along with our one page slick design - we have two of these... I have uploaded both.

```html
<!DOCTYPE html>
<html lang="en">
<head>
<meta charset="utf-8">
<title>Northgate Systems – Video Brochure Packaging</title>
<link href="https://fonts.googleapis.com/css2?family=Lato:wght@400;700&display=swap" rel="stylesheet">
<style>
  :root {
    --backdrop: #d0f1f3;
    --teal-deep: #244c5a;
    --screen-frame: #bcdee6;
    --screen: #000000;
    --navy: #1c1e2a;
    --orange: #f26a1b;
    --silver: #c9cdd3;
    --label: #ffffff;
  }
  * { box-sizing: border-box; margin: 0; padding: 0; }
  html, body { width: 1200px; height: 1200px; overflow: hidden; }
  body {
    background: var(--backdrop);
    font-family: "Lato", Arial, sans-serif;
    position: relative;
  }
  .spread {
    position: absolute;
    left: 118px;
    width: 965px;
    height: 339px;
    display: flex;
  }
  .spread--inside { top: 208px; }
  .spread--outside { top: 651px; }
  .panel { position: relative; height: 100%; overflow: hidden; }
  .panel--left { width: 482px; }
  .panel--right { width: 483px; }

  .pattern-field { background: var(--teal-deep); }
  .corner-mark {
    position: absolute;
    left: 33px; top: 283px;
    width: 24px; height: 24px;
    border-radius: 50%;
    background: var(--silver);
  }

  .screen-frame { background: var(--screen-frame); }
  .screen {
    position: absolute;
    left: 78px; top: 77px;
    width: 327px; height: 181px;
    background: var(--screen);
  }

  .back-cover, .front-cover { background: var(--navy); }

  .brand {
    position: absolute;
    display: flex;
    flex-direction: column;
    align-items: center;
    color: var(--silver);
    transform: translateX(-50%);
    text-align: center;
  }
  .brand__mark { border-radius: 50%; background: var(--silver); }
  .brand__name { font-weight: 700; letter-spacing: 0.02em; line-height: 1; }
  .brand__sub { font-weight: 700; letter-spacing: 0.08em; line-height: 1; }

  .brand--back { left: 241px; top: 238px; }
  .brand--back .brand__mark { width: 26px; height: 26px; margin-bottom: 6px; }
  .brand--back .brand__name { font-size: 11px; }
  .brand--back .brand__sub { font-size: 5px; margin-top: 2px; }

  .brand--front { left: 241px; top: 190px; z-index: 2; }
  .brand--front .brand__mark { width: 40px; height: 40px; margin-bottom: 8px; }
  .brand--front .brand__name { font-size: 17px; }
  .brand--front .brand__sub { font-size: 7px; margin-top: 3px; }

  .cover-arc { position: absolute; left: 0; top: 0; width: 483px; height: 339px; }
  .product-label {
    position: absolute;
    right: 21px; bottom: 19px;
    color: var(--label);
    font-size: 12px;
    font-weight: 400;
    letter-spacing: 0.01em;
  }
</style>
</head>
<body>
  <section class="spread spread--inside">
    <div class="panel panel--left pattern-field" role="img" aria-label="Repeating faint brand symbol pattern on deep teal">
      <span class="corner-mark"></span>
    </div>
    <div class="panel panel--right screen-frame">
      <div class="screen"></div>
    </div>
  </section>

  <section class="spread spread--outside">
    <div class="panel panel--left back-cover">
      <div class="brand brand--back">
        <span class="brand__mark"></span>
        <span class="brand__name">NORTHGATE</span>
        <span class="brand__sub">SYSTEMS, INC.</span>
      </div>
    </div>
    <div class="panel panel--right front-cover">
      <svg class="cover-arc" viewBox="0 0 483 339" preserveAspectRatio="none" aria-hidden="true">
        <path d="M0 205 Q241 410 483 205 L483 339 L0 339 Z" fill="#244c5a"/>
        <path d="M0 205 Q241 410 483 205" fill="none" stroke="#f26a1b" stroke-width="2.5"/>
      </svg>
      <div class="brand brand--front">
        <span class="brand__mark"></span>
        <span class="brand__name">NORTHGATE</span>
        <span class="brand__sub">SYSTEMS, INC.</span>
      </div>
      <span class="product-label">VIDEO BROCHURE</span>
    </div>
  </section>
</body>
</html>
```